Business card design for event company

need design double sided in square shape ( approx 6x6cm) in matt grey shades
front side :
logo ( could be in one color like picture attached ) printpress effect in a rect box

back side :
name in big font with silver foil finish ( similar to attached pic )

phone number i would like to see how it will look like if embossed ( like in credit cards )

Sample for contact on card ( will need 5 different contacts) - pls. include small icons next to each contact

KARIM SALEHI
Managing Director

+971 50 374 6619
karim@novlinkuae.com
www.novlink.ae
Building C2 , Office 318
Marsa Tirel Park

Please consider this is an urgent project . thank you in advance

```html
<!DOCTYPE html>
<html lang="en">
<head>
<meta charset="utf-8">
<title>Novlink – Business Card</title>
<link rel="stylesheet" href="https://fonts.googleapis.com/css2?family=Open+Sans:wght@400;600&family=Noto+Serif:wght@400&display=swap">
<style>
  :root {
    --page-bg: #d9d9db;
    --card-silver: #cfcfd1;
    --card-silver-light: #dcdcde;
    --ink-dark: #231f20;
    --ink-name: #4a4a4c;
    --accent-orange: #f0932b;
    --frame-grey: #5a5a5c;
  }
  * { margin: 0; padding: 0; box-sizing: border-box; }
  html, body {
    width: 1200px; height: 1200px; overflow: hidden;
    background: var(--page-bg);
  }
  .canvas { position: relative; width: 1200px; height: 1200px; }

  .card {
    position: absolute;
    background: linear-gradient(160deg, var(--card-silver-light), var(--card-silver));
    box-shadow: 0 2px 6px rgba(0,0,0,0.25);
  }
  .card--front { left: 168px; top: 164px; width: 512px; height: 508px; }
  .card--back  { left: 524px; top: 516px; width: 512px; height: 508px; text-align: center; }

  .front-brand {
    position: absolute; left: 0; right: 0; top: 224px;
    display: flex; align-items: center; justify-content: center; gap: 14px;
    font-family: "Open Sans", sans-serif; font-weight: 600;
    font-size: 50px; color: var(--ink-dark); letter-spacing: 2px;
  }
  .front-brand__square { width: 26px; height: 26px; background: var(--ink-dark); }

  .back-brand {
    position: absolute; left: 138px; top: 42px; width: 236px; height: 58px;
    border: 2px solid var(--frame-grey);
    display: flex; align-items: center; justify-content: center; gap: 10px;
    font-family: "Open Sans", sans-serif; font-weight: 400;
    font-size: 32px; color: var(--frame-grey);
  }
  .back-brand__dot { width: 10px; height: 10px; border-radius: 50%; background: var(--accent-orange); }

  .person-name {
    position: absolute; left: 0; right: 0; top: 130px;
    font-family: "Open Sans", sans-serif; font-weight: 600;
    font-size: 44px; color: var(--ink-name); letter-spacing: 1px;
    text-shadow: 1px 1px 0 #f2f2f2, -1px -1px 0 #6e6e70;
  }
  .person-title {
    position: absolute; left: 0; right: 0; top: 186px;
    font-family: "Open Sans", sans-serif; font-size: 17px;
    letter-spacing: 6px; color: var(--ink-dark);
  }
  .divider-dot {
    position: absolute; left: 249px; width: 14px; height: 14px;
    border-radius: 50%; background: var(--ink-dark);
  }
  .divider-dot--upper { top: 228px; }
  .divider-dot--lower { top: 387px; }

  .contact-phone {
    position: absolute; left: 0; right: 0; top: 262px;
    font-family: "Noto Serif", serif; font-size: 22px;
    letter-spacing: 4px; color: var(--ink-dark);
    text-shadow: 1px 1px 0 #f4f4f4;
  }
  .contact-line {
    position: absolute; left: 0; right: 0;
    font-family: "Open Sans", sans-serif; font-size: 20px; color: var(--ink-dark);
  }
  .contact-line--web { top: 302px; }
  .contact-line--mail { top: 334px; }
  .contact-line--address { top: 420px; font-size: 17px; }
</style>
</head>
<body>
<div class="canvas">
  <section class="card card--front">
    <div class="front-brand"><span class="front-brand__square"></span>NOVLINK</div>
  </section>

  <section class="card card--back">
    <div class="back-brand"><span class="back-brand__dot"></span>Novlink</div>
    <h1 class="person-name">Karim Salehi</h1>
    <p class="person-title">Managing Director</p>
    <span class="divider-dot divider-dot--upper"></span>
    <p class="contact-phone">+971 50 374 6619</p>
    <p class="contact-line contact-line--web">www.novlink.ae</p>
    <p class="contact-line contact-line--mail">karim@novlinkuae.com</p>
    <span class="divider-dot divider-dot--lower"></span>
    <p class="contact-line contact-line--address">Building C2 , Office 318, Marsa Tirel Park</p>
  </section>
</div>
</body>
</html>
```